New business card with our logo

we finalized our logo with the help of pixel harbor - now we need a business card using that logo. we are a metal service center providing raw steel and metal products for fabricating, contractors, artists, etc. we have the wording for the back of the card figured out (attached, no deviations from text please), just need help putting it all together.
would like the look of steel somehow incorporated in the design ... would like the black part of the logo to be steel or silver color (the S & BRANLEY)
Other font styles liked:
- calibri, arial, similar to those, modern looking
Colors
Designer to choose colors to be used in the design.
Requirements
Must have
- Back of card must haves are attached (no deviations from wording please).
- FRONT of card:
- logo
- address
- name
- office tel
- cell
- fax
- website
- address
Nice to have
- incorporate the look of steel or element of steel somehow
- names of the staff on front not in all caps, i.e. Rosvita not ROSVITA
- this industry is more industrial, not coffee or flower shop so design should be aligned with that
- design should be classic and tasteful

```html
<!DOCTYPE html>
<html lang="en">
<head>
<meta charset="utf-8">
<title>Branley Steel – Business Card</title>
<link href="https://fonts.googleapis.com/css2?family=Open+Sans:wght@400;600&display=swap" rel="stylesheet">
<style>
  :root {
    --backdrop: #2b2e33;
    --card-black: #060606;
    --steel: #c6c9cd;
    --accent: #d9b92e;
    --band-white: #fbfbfb;
    --text-white: #f2f2f2;
    --divider: #8a8a8a;
  }
  * { box-sizing: border-box; margin: 0; padding: 0; }
  html, body { width: 1200px; height: 900px; overflow: hidden; }
  body {
    background: var(--backdrop);
    font-family: "Open Sans", Arial, sans-serif;
    display: flex;
    align-items: center;
    justify-content: center;
    gap: 44px;
  }
  .card {
    position: relative;
    width: 540px;
    height: 310px;
    background: var(--card-black);
    border-radius: 26px;
    overflow: hidden;
    box-shadow: 0 14px 34px rgba(0,0,0,.45);
  }
  .brand {
    display: flex;
    align-items: center;
    gap: 12px;
    color: var(--steel);
    font-weight: 600;
    letter-spacing: .5px;
  }
  .brand-dot {
    border: 3px solid var(--steel);
    border-radius: 50%;
    flex: none;
  }

  /* Front */
  .card-front .brand { position: absolute; left: 150px; top: 34px; font-size: 26px; }
  .card-front .brand-dot { width: 40px; height: 40px; }
  .address {
    position: absolute; right: 28px; top: 104px;
    color: var(--text-white); font-size: 19px; font-weight: 600;
  }
  .name-band {
    position: absolute; left: 0; right: 0; top: 140px; height: 62px;
    background: var(--band-white);
    padding: 8px 0 0 30px;
    color: var(--accent);
  }
  .name { font-size: 22px; font-weight: 600; line-height: 1.1; }
  .role { font-size: 10px; line-height: 1.4; }
  .contacts {
    position: absolute; left: 30px; top: 214px;
    list-style: none;
    display: flex; flex-direction: column; gap: 7px;
  }
  .contact {
    display: flex; align-items: center; gap: 10px;
    color: var(--text-white); font-size: 13px;
  }
  .icon {
    width: 22px; height: 22px; border-radius: 50%;
    background: var(--accent);
    display: flex; align-items: center; justify-content: center; flex: none;
  }
  .divider {
    position: absolute; left: 280px; top: 220px;
    width: 1px; height: 72px; background: var(--divider);
  }
  .website {
    position: absolute; left: 306px; top: 240px;
    display: flex; align-items: center; gap: 10px;
    color: var(--text-white); font-size: 14px;
  }
  .website .icon { width: 30px; height: 30px; }

  /* Back */
  .card-back .brand {
    position: absolute; left: 0; right: 0; top: 112px;
    justify-content: center; font-size: 30px;
  }
  .card-back .brand-dot { width: 46px; height: 46px; }
  .accent-strip {
    position: absolute; left: 0; right: 0; bottom: 0; height: 40px;
    background: var(--accent);
  }
</style>
</head>
<body>

<section class="card card-front">
  <div class="brand"><span class="brand-dot"></span><span class="brand-name">BRANLEY STEEL</span></div>
  <p class="address">418,calder street, ny</p>

  <div class="name-band">
    <p class="name">Tomas Hale</p>
    <p class="role">Security Manager</p>
  </div>

  <ul class="contacts">
    <li class="contact">
      <span class="icon">
        <svg width="12" height="12" viewBox="0 0 24 24"><path fill="#060606" d="M6.6 10.8a15 15 0 0 0 6.6 6.6l2.2-2.2a1 1 0 0 1 1-.25 11.4 11.4 0 0 0 3.6.57 1 1 0 0 1 1 1V20a1 1 0 0 1-1 1A17 17 0 0 1 3 4a1 1 0 0 1 1-1h3.5a1 1 0 0 1 1 1c0 1.25.2 2.45.57 3.6a1 1 0 0 1-.25 1z"/></svg>
      </span>+000 55501 2468
    </li>
    <li class="contact">
      <span class="icon">
        <svg width="12" height="12" viewBox="0 0 24 24"><path fill="#060606" d="M7 3h10v5H7zM4 9h16a1 1 0 0 1 1 1v7h-4v4H7v-4H3v-7a1 1 0 0 1 1-1zm5 7v3h6v-3z"/></svg>
      </span>+000 55501 2468
    </li>
    <li class="contact">
      <span class="icon">
        <svg width="12" height="12" viewBox="0 0 24 24"><path fill="none" stroke="#060606" stroke-width="2.2" d="M3 6h18v12H3zM3 6l9 7 9-7"/></svg>
      </span>tomhale@mailbox.net
    </li>
  </ul>

  <span class="divider"></span>

  <div class="website">
    <span class="icon">
      <svg width="18" height="18" viewBox="0 0 24 24" fill="none" stroke="#f2f2f2" stroke-width="1.6"><circle cx="12" cy="12" r="9"/><ellipse cx="12" cy="12" rx="4" ry="9"/><path d="M3 12h18M5 7h14M5 17h14"/></svg>
    </span>www.branleysteel.com
  </div>
</section>

<section class="card card-back">
  <div class="brand"><span class="brand-dot"></span><span class="brand-name">BRANLEY STEEL</span></div>
  <span class="accent-strip"></span>
</section>

</body>
</html>
```